Brightwell Audiology Centre - is state of the art audiology clinic and needs a business card design

the card should be oriented in 'portrait' mode and have a clinic logo. The card should be double sided, with logo on the front and my details on the other side of the card

We would also like to use a tagline of 'Clarity for Every Ear'

Clinic

```html
<!DOCTYPE html>
<html lang="en">
<head>
<meta charset="utf-8">
<title>Brightwell Audiology Centre – Business Card</title>
<link rel="stylesheet" href="https://fonts.googleapis.com/css2?family=Montserrat:wght@600&family=Roboto+Condensed:wght@400;700&family=EB+Garamond:ital@1&display=swap">
<style>
  :root {
    --canvas: #ffffff;
    --shadow: #c4c4c4;
    --blue-deep: #245ba6;
    --blue-mid: #1a7cc4;
    --blue-light: #8cc8ee;
    --white: #ffffff;
    --ink: #5e5f61;
    --ink-soft: #7a7b7d;
    --frame: #c9c9c9;
  }
  html, body { margin: 0; padding: 0; overflow: hidden; }
  body { width: 1200px; height: 1001px; background: var(--canvas); position: relative; }

  .card, .card-shadow { position: absolute; width: 465px; height: 792px; }
  .card-shadow { background: var(--shadow); }
  .card-front-shadow { left: 119px; top: 122px; }
  .card-back-shadow { left: 635px; top: 121px; }

  .card-front { left: 108px; top: 111px; overflow: hidden; }
  .front-backdrop { position: absolute; inset: 0; width: 100%; height: 100%; }

  .card-back {
    left: 624px; top: 109px; background: var(--white);
    box-sizing: border-box; border: 2px solid var(--frame);
  }

  .clinic-name {
    position: absolute; margin: 0;
    font-family: "Montserrat", sans-serif; font-weight: 600;
    text-transform: uppercase; line-height: 1.18; letter-spacing: 0.5px;
  }
  .mark-dot { position: absolute; border-radius: 50%; }
  .tagline {
    position: absolute; margin: 0;
    font-family: "EB Garamond", serif; font-style: italic;
  }

  .card-front .clinic-name { left: 140px; top: 220px; font-size: 29px; color: var(--white); }
  .card-front .mark-dot { left: 62px; top: 255px; width: 48px; height: 48px; background: var(--white); }
  .card-front .tagline { left: 142px; top: 330px; font-size: 19px; color: var(--white); }

  .person { position: absolute; left: 137px; top: 92px; font-family: "Roboto Condensed", sans-serif; color: var(--ink); }
  .person-name { margin: 0; font-size: 25px; font-weight: 700; }
  .person-credentials { margin: 8px 0 0; font-size: 15px; }
  .person-role { margin: 8px 0 0; font-size: 15.5px; line-height: 1.4; }

  .card-back .clinic-name { left: 137px; top: 328px; font-size: 30px; color: var(--ink-soft); }
  .card-back .mark-dot { left: 36px; top: 362px; width: 56px; height: 56px; background: var(--blue-light); }
  .card-back .tagline { left: 134px; top: 448px; font-size: 22px; color: var(--ink); }

  .contact-list {
    position: absolute; left: 138px; top: 520px; margin: 0; padding: 0; list-style: none;
    font-family: "Roboto Condensed", sans-serif; font-size: 20px; color: var(--ink);
  }
  .contact-list li { display: flex; align-items: center; height: 32px; }
  .contact-key {
    display: inline-flex; align-items: center; justify-content: center;
    width: 19px; height: 19px; margin-right: 12px;
    background: var(--ink); color: var(--white); font-size: 15px; font-weight: 700;
  }
  .clinic-address {
    position: absolute; left: 138px; top: 662px; margin: 0;
    font-family: "Roboto Condensed", sans-serif; font-size: 19.5px; line-height: 1.4;
    color: var(--ink); font-style: normal;
  }
</style>
</head>
<body>
  <div class="card-shadow card-front-shadow"></div>
  <section class="card card-front" aria-label="Card front">
    <svg class="front-backdrop" viewBox="0 0 465 792" preserveAspectRatio="none" role="img" aria-label="Soft blue gradient backdrop">
      <defs>
        <linearGradient id="frontGradient" x1="0" y1="0" x2="1" y2="1">
          <stop offset="0" stop-color="#245ba6"/>
          <stop offset="0.55" stop-color="#1a7cc4"/>
          <stop offset="1" stop-color="#8cc8ee"/>
        </linearGradient>
      </defs>
      <rect width="465" height="792" fill="url(#frontGradient)"/>
    </svg>
    <span class="mark-dot"></span>
    <h1 class="clinic-name">Brightwell<br>Audiology<br>Centre</h1>
    <p class="tagline">Clarity for Every Ear</p>
  </section>

  <div class="card-shadow card-back-shadow"></div>
  <section class="card card-back" aria-label="Card back">
    <div class="person">
      <h2 class="person-name">Dr Arjun Mehta</h2>
      <p class="person-credentials">AuD. MSc. CCC-A. FAAA</p>
      <p class="person-role">Lead Audiologist and<br>Hearing Rehabilitation Therapist</p>
    </div>

    <span class="mark-dot"></span>
    <h2 class="clinic-name">Brightwell<br>Audiology<br>Centre</h2>
    <p class="tagline">Clarity for Every Ear</p>

    <ul class="contact-list">
      <li><span class="contact-key">M</span>9000012345</li>
      <li><span class="contact-key">P</span>0800 5550142</li>
      <li><span class="contact-key">E</span>arjun.mehta@example.com</li>
      <li><span class="contact-key">W</span>www.brightwellaudiology.in</li>
    </ul>
    <address class="clinic-address">F 1 Lakeview Arcade, Station Road,<br>Dharwad - 580 001. (Karnataka) India</address>
  </section>
</body>
</html>
```